Process Roadmap for Interior Design Firm

We are looking to ramp up the design appeal of our current process roadmap to be very visually interesting, while staying informative and descriptive about our process.

Target Market(s)

In-house Clients

Industry/Entity Type

Interior Design Firm focused on sustainable and holistic design.

Other font styles liked:
• raleway

Requirements
Must have
• 1.) it would be nice if the graphic provided a more clear indication of the “journey” from one step to the next, so that there was a clear sense of the progression (such that we are directing the viewer) 2.). We would want it to fit on an 8.5”x11” page (the page could be horizontal when we have the Calm Compass formatted out with the testimonials) (in addition to the testimonials, we may also want to have the detailed descriptions of each step of the process presented below the graphic, so that the graphic is cleaner) 3.) ideally the graphic is clear and simple enough to also be used on our Bi-Weekly Client Updates, which will be typed updates for clients re their project budgets, schedule and scope. The Calm Compass graphic (without all the testimonials) would be at the end of the update, and would fit on the page horizontally at the bottom, perhaps in a space which is 7.5”w x 4”h or so.
Should not have
• bold or bright colors. Natural neutrals are preferred, such as the ones featured on the provided graphic.

```html
<!DOCTYPE html>
<html lang="en">
<head>
<meta charset="utf-8">
<title>Calm Compass – Process Roadmap</title>
<link rel="stylesheet" href="https://fonts.googleapis.com/css2?family=Ubuntu:wght@500;700&family=Montserrat:wght@300;400&display=swap">
<style>
  :root {
    --gold: #c49c5c;
    --gold-light: #dcb980;
    --gold-dark: #8e6f3c;
    --ink: #4a4a4a;
    --body: #3f3f3f;
    --paper: #ffffff;
    --icon-bg: #f3f2f0;
    --dots: #9c9c9c;
  }
  * { box-sizing: border-box; margin: 0; padding: 0; }
  html, body { width: 1200px; height: 931px; overflow: hidden; background: #dcdbd8; }
  .roadmap {
    position: relative; width: 1200px; height: 931px; overflow: hidden;
    font-family: "Montserrat", sans-serif;
  }
  .room-photo {
    position: absolute; inset: 0;
    background:
      radial-gradient(ellipse 260px 200px at 780px 560px, rgba(120,140,90,.35), transparent 70%),
      radial-gradient(ellipse 200px 260px at 1060px 430px, rgba(210,190,160,.35), transparent 70%),
      linear-gradient(160deg, #e9e8e5 0%, #dddcd9 45%, #d3d2ce 100%);
  }
  .brand-panel { position: absolute; inset: 0; }
  .brand-pattern {
    position: absolute; left: 0; top: 466px; width: 67px; height: 155px;
    background: linear-gradient(90deg, #e6d3b0, #d8bb88);
  }
  .brand-name {
    position: absolute; color: var(--gold); font-family: "Montserrat", sans-serif;
    font-weight: 300; letter-spacing: .12em; line-height: 1;
  }
  .brand-name.line-1 { left: 103px; top: 490px; font-size: 22px; }
  .brand-name.line-2 { left: 101px; top: 527px; font-size: 36px; letter-spacing: .1em; }
  .brand-name.line-3 { left: 168px; top: 576px; font-size: 22px; letter-spacing: .18em; }

  .connectors { position: absolute; inset: 0; }

  .step-frame {
    position: absolute; border: 2.5px solid var(--gold); border-radius: 64px;
  }
  .step-card {
    position: absolute; background: var(--paper); border-radius: 58px;
    box-shadow: 6px 5px 0 #cfcdca, 8px 8px 14px rgba(0,0,0,.12);
  }
  .step-icon {
    position: absolute; width: 76px; height: 76px; border-radius: 50%;
    background: var(--icon-bg); display: flex; align-items: center; justify-content: center;
    box-shadow: 5px 6px 10px rgba(0,0,0,.22);
  }
  .step-icon svg { width: 42px; height: 42px; fill: none; stroke: var(--gold); stroke-width: 1.6; stroke-linecap: round; stroke-linejoin: round; }
  .step-title {
    position: absolute; font-family: "Ubuntu", sans-serif; font-weight: 700;
    font-size: 19px; color: var(--ink); letter-spacing: .02em; line-height: 20px;
  }
  .step-text {
    position: absolute; font-size: 8.6px; line-height: 10.3px; color: var(--body);
  }
  .step-text.justified { text-align: justify; }
  .step-number {
    position: absolute; font-family: "Ubuntu", sans-serif; font-weight: 700;
    font-size: 46px; line-height: 48px; color: var(--gold);
  }

  .testimonials {
    position: absolute; left: 940px; top: 633px; width: 218px; height: 218px; border-radius: 50%;
    background: rgba(245,244,242,.72); border: 2px dashed #555;
    box-shadow: 0 0 0 4px rgba(255,255,255,.5), 6px 8px 14px rgba(0,0,0,.12);
    text-align: center;
  }
  .testimonials-title {
    position: absolute; left: 0; right: 0; top: 55px;
    font-family: "Ubuntu", sans-serif; font-weight: 700; font-size: 19px; color: var(--ink);
  }
  .testimonials-text {
    position: absolute; left: 26px; right: 26px; top: 93px;
    font-size: 8.3px; line-height: 10.3px; color: var(--body);
  }
</style>
</head>
<body>
<main class="roadmap">
  <div class="room-photo" role="img" aria-label="Softly blurred photograph of a bright interior with plants and shelving"></div>

  <svg class="brand-panel" width="1200" height="931" viewBox="0 0 1200 931">
    <path d="M0,157 L418,499 L455,560 L455,615 Q450,660 410,700 L125,929 L0,929 Z" fill="#fff" stroke="var(--gold-light)" stroke-width="2.5"/>
    <defs>
      <linearGradient id="goldBand" x1="0" y1="0" x2="1" y2="0">
        <stop offset="0" stop-color="#c9a05f"/>
        <stop offset=".6" stop-color="#d4ae73"/>
        <stop offset="1" stop-color="#e0bf8a"/>
      </linearGradient>
      <linearGradient id="goldFold" x1="0" y1="0" x2="1" y2="1">
        <stop offset="0" stop-color="#7d6440"/>
        <stop offset="1" stop-color="#c9a36a"/>
      </linearGradient>
    </defs>
    <path d="M0,198 L302,408 Q306,424 292,430 Q282,434 268,434 L104,434 Q84,432 66,418 L0,366 Z" fill="url(#goldBand)"/>
    <path d="M162,284 L302,408 Q306,424 292,430 L270,420 Z" fill="url(#goldFold)" opacity=".9"/>
  </svg>

  <div class="brand-pattern" role="img" aria-label="Decorative gold line pattern"></div>
  <div class="brand-name line-1">LINDEN</div>
  <div class="brand-name line-2">HALE</div>
  <div class="brand-name line-3">STUDIO</div>

  <svg class="connectors" width="1200" height="931" viewBox="0 0 1200 931" fill="none" stroke="var(--dots)" stroke-width="3" stroke-dasharray="2 2.5">
    <path d="M754,164 H815 Q843,164 843,192 V232"/>
    <path d="M633,300 H576 Q548,300 548,328 V368"/>
    <path d="M493,428 H439 Q411,428 411,456 V494"/>
    <path d="M728,562 H786 Q814,562 814,590 V631"/>
    <path d="M449,699 H391 Q363,699 363,727 V767"/>
    <path d="M272,845 H248"/>
  </svg>

  <!-- 01 Listening -->
  <div class="step-frame" style="left:439px;top:100px;width:314px;height:127px"></div>
  <div class="step-card" style="left:452px;top:108px;width:293px;height:114px"></div>
  <div class="step-icon" style="left:409px;top:127px">
    <svg viewBox="0 0 42 42"><rect x="6" y="6" width="26" height="32" rx="2"/><rect x="13" y="3" width="12" height="5" rx="1"/><path d="M10 15l2 2 3-4M18 15h10M10 23l2 2 3-4M18 23h10M10 31l2 2 3-4M18 31h7"/><path d="M34 20l4 3-9 13-4 1 0-4z"/></svg>
  </div>
  <div class="step-title" style="left:519px;top:120px">LISTENING</div>
  <p class="step-text" style="left:521px;top:147px;width:132px">Listening to our clients, their land, and their home. Identifying their needs, challenges, wishes, and dreams.</p>
  <div class="step-number" style="left:670px;top:142px">01</div>

  <!-- 02 Visioning -->
  <div class="step-frame" style="left:667px;top:232px;width:367px;height:127px"></div>
  <div class="step-card" style="left:680px;top:240px;width:346px;height:114px"></div>
  <div class="step-icon" style="left:634px;top:257px">
    <svg viewBox="0 0 42 42"><path d="M15 27c-3-3-5-5-5-10a11 11 0 0 1 22 0c0 5-2 7-5 10v4H15z"/><path d="M16 34h10M17 37h8M21 2v3M6 8l2 2M36 8l-2 2M2 19h3M37 19h3M6 30l2-2M36 30l-2-2"/></svg>
  </div>
  <div class="step-title" style="left:742px;top:254px">VISIONING</div>
  <p class="step-text" style="left:742px;top:281px;width:186px">Facilitating a guided visioning process to clarify the deepest intention, true purpose, and highest potential for their home and their future within it.</p>
  <div class="step-number" style="left:951px;top:274px">02</div>

  <!-- 03 Planning -->
  <div class="step-frame" style="left:527px;top:364px;width:368px;height:127px"></div>
  <div class="step-card" style="left:540px;top:372px;width:347px;height:114px"></div>
  <div class="step-icon" style="left:494px;top:387px">
    <svg viewBox="0 0 42 42"><rect x="6" y="7" width="30" height="32" rx="2"/><rect x="15" y="3" width="12" height="6" rx="1"/><path d="M11 16l3 3M14 16l-3 3M26 29l3 3M29 29l-3 3"/><circle cx="29" cy="18" r="2.5"/><path d="M14 32c0-8 6-12 12-12M23 18l3 2-2 3"/></svg>
  </div>
  <div class="step-title" style="left:605px;top:381px">PLANNING</div>
  <p class="step-text" style="left:605px;top:413px;width:172px">Turning our client’s vision into a clearly defined scope., budg and timeline Mapping out the st for making their dre reality Setting a meeting chedule from start to</p>
  <div class="step-number" style="left:812px;top:406px">03</div>

  <!-- 04 Designing -->
  <div class="step-frame" style="left:360px;top:496px;width:368px;height:127px"></div>
  <div class="step-card" style="left:373px;top:504px;width:347px;height:114px"></div>
  <div class="step-icon" style="left:330px;top:521px">
    <svg viewBox="0 0 42 42"><path d="M8 10l4-4 28 28-4 4z"/><path d="M14 12l2-2M18 16l2-2M22 20l2-2M26 24l2-2"/><path d="M33 5l4 4L12 34l-6 2 2-6z"/><path d="M30 8l4 4"/></svg>
  </div>
  <div class="step-title" style="left:434px;top:508px">DESIGNING</div>
  <p class="step-text justified" style="left:434px;top:535px;width:198px">Following the schedule through the design Managing Coordinating with clients, builders, architects, and vendors phases from initial to ensure that the design concepts, design is executed with technical drawings and details, and the selection of all finishes, fixtures, and surnishings.</p>
  <div class="step-number" style="left:644px;top:537px">04</div>

  <!-- 05 Managing -->
  <div class="step-frame" style="left:486px;top:632px;width:369px;height:126px"></div>
  <div class="step-card" style="left:499px;top:640px;width:348px;height:113px"></div>
  <div class="step-icon" style="left:445px;top:664px">
    <svg viewBox="0 0 42 42"><rect x="4" y="7" width="28" height="25" rx="2"/><path d="M4 13h28M10 4v5M26 4v5"/><path d="M8 17h4v3H8zM15 17h4v3h-4zM22 17h4v3h-4zM8 23h4v3H8zM15 23h4v3h-4z"/><circle cx="32" cy="32" r="7" fill="#f3f2f0"/><path d="M32 28v4h3"/></svg>
  </div>
  <div class="step-title" style="left:561px;top:648px">MANAGING</div>
  <p class="step-text justified" style="left:561px;top:675px;width:202px">Coordinating with clients, builders, architects, and vendors phases from initial to ensure that the design concepts, design is executed with technical drawings and details, and the selection of all finishes, fixtures, and surnishings. excellence, and the</p>
  <div class="step-number" style="left:773px;top:672px">05</div>

  <!-- 06 Installing -->
  <div class="step-frame" style="left:219px;top:766px;width:370px;height:127px"></div>
  <div class="step-card" style="left:232px;top:774px;width:349px;height:114px"></div>
  <div class="step-icon" style="left:196px;top:796px">
    <svg viewBox="0 0 42 42"><circle cx="14" cy="21" r="4"/><path d="M14 11v-3M14 34v-3M4 21h-2M26 21h-2M7 14l-2-2M21 28l2 2M7 28l-2 2M21 14l2-2"/><circle cx="14" cy="21" r="9"/><path d="M23 17h17v8H23"/><path d="M29 17v8"/></svg>
  </div>
  <div class="step-title" style="left:307px;top:786px">INSTALLING</div>
  <p class="step-text" style="left:304px;top:817px;width:164px">Overseeing the inspection,installation and arrangement of al furnishings, lighting, artwork, and decorat- Taking care of every last detail.</p>
  <div class="step-number" style="left:505px;top:808px">06</div>

  <section class="testimonials">
    <h2 class="testimonials-title">TESTIMONIALS</h2>
    <p class="testimonials-text">Linden to send over testimonials for fill this space three or foul columns of testimonials Linden to send over testimonials for fill this space three or four</p>
  </section>
</main>
</body>
</html>
```